Textbook cover for educational dental hygiene seminar

A professional and trendy textbook cover design to be used. 8.5 x 11 with full bleed, cmyk, and a count for binding when designed. Year 2023 displayed, and title BelvaKTO’s Dental Hygiene Academy. Colors- shades of purple, white, and black. Please also use logo. Website www.BelvaKTOPrepCourse.example

For background- maybe ombré, or some sort of trendy design. Display a big tooth on the front.

Colors
6B429C
8869AF
B7A5CE
E3DAEB
F3F0F8

```html
<!DOCTYPE html>
<html lang="en">
<head>
<meta charset="utf-8">
<title>BelvaKTO’s Dental Hygiene Academy 2023 – Cover</title>
<link rel="stylesheet" href="https://fonts.googleapis.com/css2?family=Playfair+Display:wght@500&family=Montserrat:wght@500;600&family=Nunito:wght@400;800&display=swap">
<style>
  :root {
    --stage: #d4d4d4;
    --navy: #150a6b;
    --violet: #7a35d6;
    --plum-dark: #1c0636;
    --brand-purple: #6B429C;
    --brand-lilac: #8869AF;
    --brand-lavender: #B7A5CE;
    --brand-mist: #E3DAEB;
    --white: #F3F0F8;
    --accent-orange: #e38a1c;
    --accent-gold: #f2a516;
  }
  * { box-sizing: border-box; margin: 0; padding: 0; }
  html, body { width: 750px; height: 1200px; overflow: hidden; }
  body { background: var(--stage); position: relative; }

  .cover {
    position: absolute; left: 30px; top: 153px;
    width: 690px; height: 893px; overflow: hidden;
    background:
      radial-gradient(ellipse 420px 380px at 0% 48%, rgba(134, 62, 230, .95), rgba(134, 62, 230, 0) 75%),
      radial-gradient(ellipse 380px 420px at 100% 48%, var(--plum-dark), rgba(28, 6, 54, 0) 80%),
      linear-gradient(180deg, var(--navy) 0%, #3d169a 55%, #2a0f8a 100%);
  }
  .cover__art { position: absolute; inset: 0; width: 690px; height: 893px; }

  .title { position: absolute; left: 0; right: 0; text-align: center; color: #fff; }
  .title__owner {
    top: 58px; font-family: "Playfair Display", serif; font-weight: 500;
    font-size: 58px; line-height: 1; letter-spacing: -1px; transform: scaleX(.9);
  }
  .title__main {
    top: 120px; font-family: "Montserrat", sans-serif; font-weight: 600;
    font-size: 100px; letter-spacing: 1px; line-height: 1;
  }
  .title__sub {
    top: 208px; font-family: "Montserrat", sans-serif; font-weight: 600;
    font-size: 39px; letter-spacing: .5px; line-height: 1;
  }
  .title__year {
    top: 255px; font-family: "Montserrat", sans-serif; font-weight: 600;
    font-size: 40px; line-height: 1;
  }

  .brand-mark {
    position: absolute; left: 185px; top: 396px; width: 320px; height: 320px;
    border-radius: 50%; background: var(--brand-purple);
    border: 10px solid var(--brand-mist);
    display: flex; align-items: center; justify-content: center; text-align: center;
  }
  .brand-mark__name {
    width: 220px; font-family: "Montserrat", sans-serif; font-weight: 600;
    font-size: 27px; line-height: 1.25; color: var(--white);
  }

  .tagline {
    position: absolute; left: 0; right: 0; top: 795px; text-align: center;
    font-family: "Nunito", sans-serif; font-weight: 800; font-size: 22px; line-height: 1.2; color: #fff;
  }
  .website {
    position: absolute; left: 0; right: 0; top: 826px; text-align: center;
    font-family: "Nunito", sans-serif; font-weight: 400; font-size: 19px; line-height: 1.2; color: #fff;
  }
  .website strong { font-weight: 800; }
</style>
</head>
<body>
  <main class="cover">
    <svg class="cover__art" viewBox="0 0 690 893">
      <defs>
        <radialGradient id="illustration-tone" cx=".6" cy=".55" r=".6">
          <stop offset="0" stop-color="#8a45b8" stop-opacity=".45"/>
          <stop offset="1" stop-color="#8a45b8" stop-opacity="0"/>
        </radialGradient>
      </defs>
      <rect class="illustration-area" x="380" y="330" width="310" height="563" fill="url(#illustration-tone)"
            role="img" aria-label="Purple toothbrush illustration behind the badge"/>
      <path class="accent-curve" d="M0 392 C 90 350, 190 260, 262 110" fill="none" stroke="var(--accent-orange)" stroke-width="1.5" opacity=".8"/>
      <path class="accent-curve" d="M690 518 C 600 570, 500 620, 440 700" fill="none" stroke="#c0392b" stroke-width="1.5" opacity=".8"/>
      <path d="M48 510 L68 492 M600 340 L612 330" stroke="var(--accent-orange)" stroke-width="1.2" opacity=".7"/>
      <circle cx="331" cy="270" r="12" fill="none" stroke="var(--accent-orange)" stroke-width="1" opacity=".5"/>
      <circle cx="206" cy="770" r="28" fill="none" stroke="var(--accent-orange)" stroke-width="1" opacity=".45"/>
      <line x1="138" y1="276" x2="285" y2="276" stroke="#fff" stroke-width="1.2"/>
      <line x1="405" y1="276" x2="550" y2="276" stroke="#fff" stroke-width="1.2"/>
      <circle cx="123" cy="272" r="6" fill="var(--accent-orange)"/>
      <circle cx="543" cy="445" r="7" fill="var(--accent-gold)"/>
    </svg>

    <p class="title title__owner">BELVAKTO’S</p>
    <h1 class="title title__main">DENTAL</h1>
    <p class="title title__sub">HYGIENE ACADEMY</p>
    <p class="title title__year">2023</p>

    <div class="brand-mark">
      <span class="brand-mark__name">BelvaKTO’s Dental Hygiene Academy</span>
    </div>

    <p class="tagline">The World’s First Interactive Review Book!</p>
    <p class="website">www.<strong>BelvaKTOPrepCourse</strong>.example</p>
  </main>
</body>
</html>
```